we have the following Products we need designs for.
1: Coconut Milk 425ml
2: Coconut Cream 425g
3: Tinned Fruit Cocktail 850g
4: Tinned Sliced Peaches 850g
5: Tinned Pears. 850g
I have attached a few ideas our customer had as well as Ingredients and Nutritional Info. ( Note for Australia we need NIP to be for serving size and 100g/ml) also attached example.

Target Market(s)

Supermarkets

Requirements
Must have
• Brand Name is Wandeen colours can be different

```html
<!DOCTYPE html>
<html lang="en">
<head>
<meta charset="utf-8">
<title>Coconut Cream – Nutrition Label</title>
<link rel="stylesheet" href="https://fonts.googleapis.com/css2?family=Tinos:ital,wght@0,400;0,700;1,400&family=Open+Sans:wght@400;600;700&family=Oswald:wght@400;500;600&family=Anton&display=swap">
<style>
:root{
  --workspace:#5b5b5b;
  --ink:#151515;
  --frame:#1b191a;
  --purple:#3d1752;
  --purple-soft:#6b4190;
  --pink:#e0307a;
  --paper:#ffffff;
  --wood-white:#eef0f2;
  --flag-red:#d92b2b;
}
*{box-sizing:border-box;margin:0;padding:0}
html,body{width:1200px;height:803px;overflow:hidden;background:var(--workspace)}
.stage{position:absolute;left:0;top:0;width:1293px;height:865px;transform:scale(.928);transform-origin:0 0;background:var(--workspace);color:var(--ink)}
.abs{position:absolute}

/* spec sheet */
.spec-title{left:40px;top:30px;font:400 20px/24px "Open Sans",sans-serif;white-space:nowrap}
.spec-title .big{font-size:23px}
.spec-size{left:40px;top:764px;font:400 20px/24px "Open Sans",sans-serif}
.facts{left:96px;top:58px;width:529px;height:700px;border:2px solid var(--ink);font-family:"Tinos",serif;font-size:18px}
.row{position:absolute;left:0;right:0;border-bottom:1.5px solid var(--ink);display:flex;align-items:center;padding:0 3px}
.row.thick{border-bottom-width:5px}
.row .name{flex:1}
.row .amt{width:120px;text-align:center;position:absolute;left:318px}
.row .dv{position:absolute;right:3px}
.b{font-weight:700}
.indent{padding-left:100px}
.foot{position:absolute;left:12px;right:0;font-size:15.5px}

/* label */
.frame{left:925px;top:0;width:368px;height:853px;background:var(--frame)}
.label{left:1005px;top:0;width:288px;height:772px;background:var(--wood-white);border:3px solid var(--pink);border-top:none;border-right:none;overflow:hidden}
.palm{left:200px;top:0;width:90px;height:260px;background:linear-gradient(200deg,#2f7a22,#7fb94a 55%,rgba(238,240,242,0) 80%)}
.sandphoto{left:205px;top:250px;width:90px;height:530px;background:linear-gradient(180deg,#e7dccb,#d6bf9e 55%,#b89670)}
.panel{left:10px;top:182px;width:205px;height:384px;background:var(--purple);clip-path:polygon(0 0,100% 1%,97% 100%,0 100%)}
.heading{left:32px;top:68px;font:500 29px/32px "Oswald",sans-serif;color:var(--purple);letter-spacing:.3px}
.heading-big{left:24px;top:94px;font:400 96px/96px "Anton",sans-serif;color:var(--purple);letter-spacing:1px}
.nip{left:18px;top:205px;width:185px;color:#fff;font-family:"Open Sans",sans-serif}
.nline{position:absolute;left:0;right:0;font-size:12px;line-height:14px;white-space:nowrap}
.nline .q{position:absolute;left:104px;width:44px;text-align:right}
.nline .p{position:absolute;left:152px;width:32px;text-align:right}
.nline.sub{font-size:10.5px}
.nline.h{font-weight:600;font-size:12.5px}
.colhead{position:absolute;top:36px;font-size:8px;line-height:12px;text-align:right;white-space:nowrap}
.note{left:16px;top:579px;width:200px;font:600 10px/12px "Open Sans",sans-serif;color:var(--purple)}
.ing-title{left:20px;top:645px;font:500 22px/28px "Oswald",sans-serif;color:var(--purple-soft)}
.ing{left:16px;top:675px;width:160px;font:600 10px/12px "Open Sans",sans-serif;color:var(--purple)}
.origin{left:125px;top:734px;width:70px;text-align:center;font:700 8px/9px "Oswald",sans-serif;color:var(--purple)}
</style>
</head>
<body>
<div class="stage">
  <div class="abs spec-title">2.&nbsp; Coconut cream : <span class="big">Ingredient:</span>&nbsp; Coconut Extract (50%), Water, Thickener (Guar Gum)</div>

  <div class="abs facts">
    <div class="row" style="top:0;height:40px;justify-content:center;border-bottom:none">4 serving per container</div>
    <div class="row thick b" style="top:40px;height:24px"><span class="name">Serving size</span><span class="dv">3.38 fl. oz (100 mL)</span></div>
    <div class="row thick" style="top:64px;height:64px;align-items:flex-start;flex-direction:column;padding-top:2px">
      <span class="b">Amount Per Serving</span>
      <span class="b" style="font-size:40px;line-height:36px">Calories</span>
      <span class="b" style="position:absolute;right:30px;top:24px;font-size:28px">60</span>
    </div>
    <div class="row b" style="top:128px;height:42px;justify-content:flex-end;font-size:15px">% Daily Value *</div>
    <div class="row" style="top:170px;height:25px"><span class="name b">Total Fat</span><span class="amt">6 g</span><span class="dv">8%</span></div>
    <div class="row indent" style="top:195px;height:26px"><span class="name">Saturated Fat</span><span class="amt">5 g</span><span class="dv">25%</span></div>
    <div class="row indent" style="top:221px;height:39px;align-items:flex-start;padding-left:117px"><span class="name"><i>Trans</i> Fat</span><span class="amt">0 g</span></div>
    <div class="row" style="top:260px;height:25px"><span class="name b">Cholesterol</span><span class="amt">0 mg</span><span class="dv">0%</span></div>
    <div class="row" style="top:285px;height:26px"><span class="name b">Sodium</span><span class="amt">15 mg</span><span class="dv">1%</span></div>
    <div class="row" style="top:311px;height:27px"><span class="name b">Total Carbohydrate</span><span class="amt">1 g</span><span class="dv">0%</span></div>
    <div class="row indent" style="top:338px;height:24px"><span class="name">Dietary Fiber</span><span class="amt">0 g</span><span class="dv">0%</span></div>
    <div class="row indent" style="top:362px;height:39px;align-items:flex-start"><span class="name">Total Sugars</span><span class="amt">&lt; 1 g</span></div>
    <div class="row" style="top:401px;height:24px;padding-left:107px;font-size:16px"><span class="name">Includes &nbsp; &nbsp; &nbsp; &nbsp; &nbsp; g Added Sugars</span></div>
    <div class="row thick" style="top:425px;height:40px;align-items:flex-start"><span class="name b">Protein</span><span class="amt">&lt; 1 g</span></div>
    <div class="row" style="top:465px;height:27px"><span class="name">Vitamin D</span><span class="amt">0 mcg</span><span class="dv">0%</span></div>
    <div class="row" style="top:492px;height:26px"><span class="name">Calcium</span><span class="amt">2 mg</span><span class="dv">0%</span></div>
    <div class="row" style="top:518px;height:26px"><span class="name">Iron</span><span class="amt">0 mg</span><span class="dv">0%</span></div>
    <div class="row" style="top:544px;height:26px"><span class="name">Potassium</span><span class="amt">40 mg</span><span class="dv">0%</span></div>
    <div class="foot" style="top:624px;white-space:nowrap;overflow:hidden">* The % Daily Values (DV) tells you how much a nutrient in a serving of food</div>
    <div class="foot" style="top:667px;left:25px">contributes to a daily diet. 2,000 calories a day is used for gerneral advice.</div>
  </div>
  <div class="abs spec-size">Label size :&nbsp;&nbsp;&nbsp; 247*99mm</div>

  <div class="abs frame"></div>
  <div class="abs label">
    <div class="abs palm" role="img" aria-label="Photo of green palm fronds"></div>
    <div class="abs sandphoto" role="img" aria-label="Photo of sand on a wooden board"></div>
    <div class="abs heading">NUTRITIONAL</div>
    <div class="abs heading-big">INFO</div>
    <div class="abs panel"></div>
    <div class="abs nip">
      <div class="nline h" style="top:0">Servings / package:<span class="q" style="left:140px">4g</span></div>
      <div class="nline h" style="top:16px">Servings size:<span class="q" style="left:140px">100ml</span></div>
      <div class="colhead" style="right:40px">Average<br>Quantity per<br>Serving Calories 60</div>
      <div class="colhead" style="right:1px">Average<br>Quantity<br>per 100g</div>
      <div class="nline" style="top:81px">Fat, total<span class="q">6g</span><span class="p">8%</span></div>
      <div class="nline sub" style="top:97px">&nbsp;- Saturated<span class="q">5g</span><span class="p">25%</span></div>
      <div class="nline sub" style="top:114px">&nbsp;- Trans Fat<span class="q">0g</span></div>
      <div class="nline" style="top:137px">Cholesterol<span class="q">0mg</span><span class="p">0%</span></div>
      <div class="nline" style="top:161px">Sodium<span class="q">15mg</span><span class="p">1%</span></div>
      <div class="nline" style="top:184px">Carbohydrate<span class="q">1g</span><span class="p">0%</span></div>
      <div class="nline sub" style="top:199px">&nbsp;- Dietry Fibre<span class="q">0g</span><span class="p">0%</span></div>
      <div class="nline sub" style="top:215px">&nbsp;- Total Sugars<span class="q" style="width:30px;left:100px">&lt;1g</span></div>
      <div class="nline sub" style="top:230px">&nbsp;- Includes 0g Added Sugars</div>
      <div class="nline" style="top:254px">Protein<span class="q">&lt;1g</span></div>
      <div class="nline" style="top:277px">Vitamin D<span class="q">0mg</span><span class="p">0%</span></div>
      <div class="nline" style="top:293px">Calcium<span class="q">2mg</span><span class="p">0%</span></div>
      <div class="nline" style="top:310px">Iron<span class="q">0mg</span><span class="p">0%</span></div>
      <div class="nline" style="top:326px">Potassium<span class="q">40g</span><span class="p">0%</span></div>
    </div>
    <div class="abs note">The % Daily Values (DV) tells you how much a nutrient in a serving of food contributes to a daily diet.<br>2,000 calories a day is used for general advice.</div>
    <div class="abs ing-title">INGREDIENTS</div>
    <div class="abs ing">Coconut Extract (50%), Water, Thickener (guar Gum)</div>
    <svg class="abs" style="left:14px;top:712px" width="110" height="46" viewBox="0 0 110 46" role="img" aria-label="Recycle and bin icons">
      <circle cx="22" cy="24" r="18" fill="none" stroke="var(--purple)" stroke-width="6"/>
      <rect x="62" y="16" width="26" height="28" fill="var(--purple)"/>
      <rect x="58" y="10" width="34" height="4" fill="var(--purple)"/>
    </svg>
    <svg class="abs" style="left:143px;top:698px" width="34" height="34" viewBox="0 0 34 34" aria-hidden="true">
      <circle cx="17" cy="17" r="16" fill="var(--flag-red)"/>
    </svg>
    <div class="abs origin">PRODUCT<br>MADE IN CHINA</div>
  </div>
</div>
</body>
</html>
```